FinTech company looking to revamp and expand client-facing interface for our financial models

Halvern Quotient currently has a very simple website that allows clients to interact with our financial models. We are looking to completely redesign the current site and add several extra pages to provide extra functionality. We want the design to have a modern, slick feel, that will work on both a desktop or a tablet. It should be straightforward for clients to move between different pages at any time, and clear from the layout how to interact with the more advanced features. We have included screenshots of existing pages in the attached design brief, as well as sketches of the functionality required by the new pages, but can't provide a direct link to the current site.
Target Market(s)
Professional investors that will be paying to access the interface
Industry/Entity Type
Finance
Number of Pages Required
4 page
Colors
Designer to choose colors to be used in the design.
Look and feel
Each slider illustrates characteristics of the customer's brand and the style your logo design should communicate.

```html
<!DOCTYPE html>
<html lang="en">
<head>
<meta charset="utf-8">
<title>HQLAB – Models</title>
<link href="https://fonts.googleapis.com/css2?family=Roboto:wght@400;500&display=swap" rel="stylesheet">
<style>
:root{
  --bar:#3d3d39;
  --bar-active:#2c2c29;
  --ink:#222;
  --muted:#555;
  --line:#8a8a8a;
  --blue:#0d57a8;
  --row-light:#f0efef;
  --row-dark:#dcdbdb;
  --cell-line:#c4c4c4;
  --white:#fff;
}
*{box-sizing:border-box;margin:0;padding:0}
html,body{width:1200px;height:866px;overflow:hidden}
body{position:relative;background:var(--white);font-family:'Roboto',Arial,sans-serif;color:var(--ink)}
.topbar{position:absolute;left:0;top:0;width:1200px;height:70px;background:var(--bar);color:var(--white)}
.brand{position:absolute;left:197px;top:20px;font-size:22px;font-weight:400;letter-spacing:.5px}
.tabs{position:absolute;left:318px;top:0;display:flex;height:70px}
.tab{display:flex;align-items:center;justify-content:center;height:70px;font-size:13px;padding:0 15px}
.tab.is-active{background:var(--bar-active)}
.mainnav{position:absolute;right:176px;top:27px;display:flex;gap:21px;font-size:13px;font-weight:500}
.mainnav span{display:flex;align-items:center;gap:4px}
.mainnav svg{width:13px;height:13px;fill:var(--white)}

.filter-label{position:absolute;left:172px;top:124px;font-size:13px}
.filter-box{position:absolute;left:172px;width:405px;border:1px solid var(--line);background:var(--white)}
.filter-all{top:148px;height:54px}
.filter-list{top:208px;height:169px;overflow:hidden}
.filter-row{position:absolute;left:0;width:386px;height:55px;font-size:13px;color:#333}
.filter-row .name{position:absolute;top:20px}
.filter-row .radio{position:absolute;top:21px;width:12px;height:12px;border-radius:50%;border:1px solid #888;background:#eee}
.filter-row .radio::after{content:"";position:absolute;left:2px;top:2px;width:6px;height:6px;border-radius:50%;background:#999}
.filter-row .radio.on::after{background:#666}
.filter-row .thr{position:absolute;left:82px;top:20px}
.slider{position:absolute;left:165px;top:19px;width:143px;height:12px}
.slider .track{position:absolute;left:0;top:5px;width:143px;height:2px;background:#555}
.slider .tick{position:absolute;top:0;width:2px;height:12px;background:#555}
.slider .lo{position:absolute;left:-2px;top:14px;font-size:12px}
.slider .hi{position:absolute;left:131px;top:14px;font-size:12px}
.divider{position:absolute;left:0;width:386px;height:1px;background:#c8c8c8}
.chev{position:absolute;right:12px;top:20px;width:12px;height:12px}
.vscroll{position:absolute;right:0;top:0;width:10px;height:167px;background:#f3f3f3;border-left:1px solid #ddd}
.vscroll .thumb{position:absolute;left:3px;top:48px;width:4px;height:52px;background:#555;border-radius:2px}

.export{position:absolute;left:172px;top:395px;font-size:13px;display:flex;align-items:center;gap:4px}
.export svg{width:12px;height:12px}
.hscroll{position:absolute;left:457px;top:399px;width:570px;height:15px;border:1px solid #ccc;background:#f7f7f7}
.hscroll .btn{position:absolute;top:-1px;width:19px;height:15px;background:var(--bar)}
.hscroll .btn svg{width:19px;height:15px}
.hscroll .thumb{position:absolute;left:30px;top:2px;width:184px;height:10px;background:#666;border-radius:5px}

.models{position:absolute;left:172px;top:424px;border-collapse:collapse;table-layout:fixed;box-shadow:0 4px 8px rgba(0,0,0,.25)}
.models th{height:48px;background:var(--blue);color:var(--white);font-size:13px;font-weight:400;border-right:1px solid #3a78bd;text-align:center}
.models td{height:49px;font-size:11px;text-align:center;border-right:1px solid var(--cell-line);border-bottom:1px solid var(--cell-line);line-height:1.3}
.models tr:nth-child(odd) td{background:var(--row-light)}
.models tr:nth-child(even) td{background:var(--row-dark)}
.models th svg{width:9px;height:6px;margin-left:8px;vertical-align:middle}
.add-column{position:absolute;left:1028px;top:424px;width:59px;height:48px;background:var(--bar);color:var(--white);font-size:12px;text-align:center;line-height:14px;padding-top:11px;box-shadow:2px 3px 6px rgba(0,0,0,.35)}
.add-column svg{position:absolute;right:4px;top:4px;width:11px;height:11px}

.fav-btn{position:absolute;left:866px;top:737px;width:161px;height:44px;background:var(--bar);color:var(--white);font-size:14px;display:flex;align-items:center;justify-content:center;gap:7px}
.fav-btn svg{width:12px;height:12px}

.footer{position:absolute;left:0;top:804px;width:1200px;height:62px;background:var(--bar);color:var(--white);font-size:12px;text-align:center;line-height:62px}
</style>
</head>
<body>
<header class="topbar">
  <div class="brand">HQLAB</div>
  <nav class="tabs">
    <div class="tab is-active">250D</div>
    <div class="tab" style="padding:0 17px 0 19px">83D</div>
    <div class="tab" style="padding:0 15px 0 14px">42D</div>
  </nav>
  <nav class="mainnav">
    <span><svg viewBox="0 0 16 16"><path d="M8 1 0 8h2v7h4v-5h4v5h4V8h2z"/></svg>MODELS</span>
    <span><svg viewBox="0 0 16 16"><path d="M7 0h2l.5 2.2 1.6.7 1.9-1.2 1.4 1.4-1.2 1.9.7 1.6L16 7v2l-2.2.5-.7 1.6 1.2 1.9-1.4 1.4-1.9-1.2-1.6.7L9 16H7l-.5-2.2-1.6-.7-1.9 1.2-1.4-1.4 1.2-1.9-.7-1.6L0 9V7l2.2-.5.7-1.6-1.2-1.9 1.4-1.4 1.9 1.2 1.6-.7zM8 5a3 3 0 1 0 0 6 3 3 0 0 0 0-6z"/></svg>SENSITIVITIES</span>
    <span><svg viewBox="0 0 16 16"><path d="M8 0l2.4 5.2 5.6.6-4.2 3.8 1.2 5.6L8 12.4 3 15.2l1.2-5.6L0 5.8l5.6-.6z"/></svg>FAVOURITES</span>
  </nav>
</header>

<div class="filter-label">Filter</div>
<div class="filter-box filter-all">
  <div class="filter-row" style="top:0">
    <span class="name" style="left:19px">ALL</span>
    <span class="radio on" style="left:53px"></span>
    <span class="thr">THRESHOLD</span>
    <div class="slider"><div class="track"></div><div class="tick" style="left:0"></div><div class="tick" style="left:141px"></div><span class="lo">0</span><span class="hi">100</span></div>
  </div>
  <svg class="chev" viewBox="0 0 12 12"><path d="M2 4l4 4 4-4" fill="none" stroke="#333" stroke-width="1.5"/></svg>
</div>

<div class="filter-box filter-list">
  <div class="filter-row" style="top:6px">
    <span class="name" style="left:10px">STAT1</span><span class="radio" style="left:53px"></span>
    <span class="thr">THRESHOLD</span>
    <div class="slider"><div class="track"></div><div class="tick" style="left:0"></div><div class="tick" style="left:141px"></div><span class="lo">0</span><span class="hi">100</span></div>
  </div>
  <div class="divider" style="top:59px"></div>
  <div class="filter-row" style="top:61px">
    <span class="name" style="left:9px">STAT2</span><span class="radio" style="left:53px"></span>
    <span class="thr">THRESHOLD</span>
    <div class="slider"><div class="track"></div><div class="tick" style="left:0"></div><div class="tick" style="left:141px"></div><span class="lo">0</span><span class="hi">100</span></div>
  </div>
  <div class="divider" style="top:114px"></div>
  <div class="filter-row" style="top:112px">
    <span class="name" style="left:9px">STAT3</span><span class="radio" style="left:53px"></span>
    <span class="thr">THRESHOLD</span>
    <div class="slider"><div class="track"></div><div class="tick" style="left:0"></div><div class="tick" style="left:141px"></div><span class="lo">0</span><span class="hi">100</span></div>
  </div>
  <div class="vscroll"><div class="thumb"></div></div>
</div>

<div class="export"><svg viewBox="0 0 12 12"><path d="M4 1h4v4h3L6 10 1 5h3z M1 11h10" fill="#222" stroke="#222"/></svg>Export</div>
<div class="hscroll">
  <div class="btn" style="left:-1px"><svg viewBox="0 0 19 15"><path d="M11 4l-4 3.5 4 3.5" fill="none" stroke="#fff" stroke-width="1.5"/></svg></div>
  <div class="thumb"></div>
  <div class="btn" style="right:-1px"><svg viewBox="0 0 19 15"><path d="M8 4l4 3.5-4 3.5" fill="none" stroke="#fff" stroke-width="1.5"/></svg></div>
</div>

<table class="models">
  <colgroup>
    <col style="width:71px"><col style="width:72px"><col style="width:70px"><col style="width:72px">
    <col style="width:71px"><col style="width:71px"><col style="width:71px"><col style="width:71px">
    <col style="width:71px"><col style="width:72px"><col style="width:71px"><col style="width:72px">
  </colgroup>
  <thead>
    <tr><th>ID<svg viewBox="0 0 9 6"><path d="M0 0h9L4.5 6z" fill="#fff"/></svg></th><th>SECTOR</th><th>TIME</th><th>QUALITY</th><th>STAT1</th><th>STAT2</th><th>STAT3</th><th>STAT4</th><th>STAT5</th><th>STAT6</th><th>STAT7</th><th>STAT8</th></tr>
  </thead>
  <tbody>
    <tr><td>Model 1</td><td>Materials</td><td>2019-07-03<br>12:15:00.000</td><td>30.2288</td><td>2.01574</td><td>23.305</td><td>-0.149368</td><td>22.3054</td><td>4.63714</td><td>0.945706</td><td>2.81949</td><td>2.60858</td></tr>
    <tr><td>Model 2</td><td>Industrials</td><td>2019-07-03<br>12:15:00.000</td><td>32.8694</td><td>0.87307</td><td>32.185</td><td>-0.0336927</td><td>33.9911</td><td>11.5693</td><td>-0.472968</td><td>-0.830458</td><td>6.80646</td></tr>
    <tr><td>Model 3</td><td>Consumer<br>Discretionary</td><td>2019-07-03<br>12:15:00.000</td><td>1.66002</td><td>-0.569222</td><td>159.814</td><td>0.0252328</td><td>172.616</td><td>10.2875</td><td>-0.750396</td><td>-0.385309</td><td>4.69146</td></tr>
    <tr><td>Model 4</td><td>Information<br>Technology</td><td>2019-07-03<br>12:15:00.000</td><td>45.6856</td><td>0.412148</td><td>202.488</td><td>0.00849232</td><td>205.834</td><td>11.9094</td><td>-0.137913</td><td>-0.449595</td><td>3.85106</td></tr>
    <tr><td>Model 5</td><td>Information<br>Technology</td><td>2019-07-03<br>12:15:00.000</td><td>75.7733</td><td>7.06728</td><td>188.605</td><td>0.016913</td><td>181.665</td><td>3.82241</td><td>0.981019</td><td>1.29847</td><td>3.34927</td></tr>
  </tbody>
</table>
<div class="add-column">ADD<br>COLUMN<svg viewBox="0 0 12 12"><circle cx="6" cy="6" r="6" fill="#fff"/><path d="M6 3v6M3 6h6" stroke="#3d3d39" stroke-width="1.6"/></svg></div>

<div class="fav-btn"><svg viewBox="0 0 12 12"><circle cx="6" cy="6" r="6" fill="#fff"/><path d="M6 3v6M3 6h6" stroke="#3d3d39" stroke-width="1.6"/></svg>Add to Favourites</div>

<footer class="footer">©Copyright information here</footer>
</body>
</html>
```